Landing page for a cyber security service provider called 'Quill Vantor'

The client is a new cyber security company in need of a website landing page at quillvantor.com.

Their visual identity is modern, playful, clean and uncluttered and represents innovation, connectivity and approachability.

The company logo is provided in black (attached) but the client is open to changing the colour to align with the new website design.

The landing page needs to contain:
- A call to action with a 'Get Started' button
-Links to blank 'How it works', 'Products', 'Pricing', 'About Us' and 'Contact Us' pages (that we'll fill out later)

Target Market(s)

Medium to large businesses who probably don't understand cyber / cyber security but need their business to be protected.

Industry/Entity Type

Cyber Security

Coding

Coded - Design and coding required

Number of Pages Required

1 page

Font styles to use
Sans Serif
Other font styles liked:
• Helvetica

Requirements
Nice to have
• Hero banner at the top of the landing page.
Should not have
• Should not look like a traditional cyber / cyber security design (eg no dark blue/ black, red/black colour combinations). Please no military styles (eg no shields, cannons, swords, guns)

```html
<!DOCTYPE html>
<html lang="en">
<head>
<meta charset="utf-8">
<title>Quill Vantor — Cyber Security</title>
<link rel="stylesheet" href="https://fonts.googleapis.com/css2?family=Jost:wght@400;500;600;700&family=Tilt+Warp&display=swap">
<style>
:root{
  --teal:#2e5358;
  --teal-dark:#24454a;
  --orange:#f7811d;
  --text:#555c5e;
  --muted:#7a8284;
  --line:#c9cfd0;
  --mist:#eef1f2;
  --white:#ffffff;
}
*{box-sizing:border-box;margin:0;padding:0}
html,body{width:1200px;height:4922px;overflow:hidden}
body{font-family:'Jost',sans-serif;color:var(--text);background:var(--white);position:relative}
.abs{position:absolute}
.display{font-family:'Tilt Warp',sans-serif;color:var(--teal);font-weight:400}
.btn{position:absolute;background:var(--orange);color:var(--white);font-size:13px;font-weight:500;display:flex;align-items:center;justify-content:center;gap:6px;border-radius:3px}
.btn .dot{width:11px;height:11px;border:1.5px solid var(--white);border-radius:50%}

/* header */
.brand{left:51px;top:0;width:105px;height:105px;background:#1d2a2c;display:flex;align-items:center;justify-content:center;color:var(--white);font-weight:600;font-size:17px;text-align:center;line-height:1.1;box-shadow:0 2px 6px rgba(0,0,0,.25)}
.topbar{top:12px;left:543px;display:flex;align-items:center;gap:14px;font-size:14px;color:#333}
.topbar span{display:flex;align-items:center;gap:7px}
.social-dot{width:17px;height:17px;border-radius:50%;background:var(--teal);display:inline-block}
.inquiry{left:1013px;top:4px;width:140px;height:34px}
.nav{top:70px;left:536px;display:flex;gap:0;font-size:16px;color:#333;font-weight:500}
.nav a{color:inherit;text-decoration:none;padding:0 10px;border-left:1px solid #999;line-height:14px}
.nav a:first-child{border-left:none;color:var(--orange)}

/* hero */
.hero-sky{left:0;top:118px;width:1200px;height:480px;background:linear-gradient(180deg,#f3f5f6 0%,#e5eaeb 60%,#f8f9f9 100%)}
.hero-art{left:440px;top:118px}
.hero-title{left:42px;top:255px;font-size:66px;line-height:64px}
.hero-sub{left:42px;top:410px;font-size:21px;color:#222;font-weight:500}
.hero-sub b{color:var(--orange);font-weight:700;font-size:24px}
.hero-btn{left:42px;top:461px;width:164px;height:34px}

.offer{top:587px;width:541px;height:200px;background:var(--teal);border-radius:10px;color:var(--white)}
.offer svg{position:absolute;left:16px;top:16px}
.offer h3{position:absolute;left:141px;top:36px;font-size:23px;font-weight:500}
.offer p{position:absolute;left:141px;top:78px;width:378px;font-size:13px;line-height:20px}
.offer .more{position:absolute;right:32px;bottom:25px;color:var(--orange);font-size:13px;font-weight:500}

/* about */
.orbit{left:51px;top:880px}
.about-title{left:606px;top:1010px;font-size:38px}
.about-text{left:606px;top:1068px;width:542px;font-size:13px;line-height:20.5px;text-align:justify;color:var(--muted)}
.about-btn{left:606px;top:1242px;width:162px;height:36px}

/* how */
.how-band{left:0;top:1505px;width:1200px;height:515px;background:linear-gradient(180deg,#fff 0%,var(--mist) 12%,var(--mist) 88%,#fff 100%)}
.how-title{left:0;width:1200px;top:1555px;font-size:38px;text-align:center}
.how-intro{left:42px;top:1619px;width:1116px;font-size:13px;line-height:20px;color:var(--muted)}
.step{top:1720px;width:265px;text-align:center}
.step svg{display:block;margin:0 auto}
.step h4{font-size:18px;font-weight:500;color:#333;margin-top:22px}
.step p{font-size:13px;line-height:20px;color:var(--muted);margin-top:8px}

/* products */
.prod-title{left:0;width:1200px;top:2104px;font-size:38px;text-align:center}
.box{top:2200px;width:160px;height:230px}
.prod-name{top:2462px;width:300px;text-align:center;font-size:18px;color:#333;font-weight:500}
.features{top:2512px;width:266px;list-style:none;font-size:13px;line-height:20px;color:var(--muted)}
.features li{position:relative;padding-left:16px;margin-bottom:14px}
.features li::before{content:"";position:absolute;left:0;top:8px;width:5px;height:5px;border-radius:50%;background:#555}
.features b{display:block;color:var(--teal);font-weight:600}
.features .j{text-align:justify}

/* pricing */
.price-title{left:0;width:1200px;top:3125px;font-size:38px;text-align:center}
.plan{top:3210px;width:329px;height:514px;background:var(--teal);color:var(--white);overflow:hidden}
.plan h3{position:absolute;left:27px;top:22px;font-size:27px;font-weight:600}
.plan hr{position:absolute;left:27px;top:64px;width:275px;border:none;border-top:1px solid #6c8a8e}
.plan .amt{position:absolute;left:27px;top:80px;font-size:24px;color:var(--orange);font-weight:500}
.plan .amt small{font-size:13px}
.plan ul{position:absolute;left:27px;top:140px;list-style:none}
.plan li{height:38.4px;display:flex;align-items:flex-start;gap:10px;font-size:11.5px;font-weight:600}
.plan li svg{flex:none}
.ribbon{position:absolute;right:-34px;top:22px;width:140px;height:24px;background:var(--orange);transform:rotate(45deg);font-size:9px;font-weight:700;display:flex;align-items:center;justify-content:center;letter-spacing:.5px}

/* contact */
.contact-card{left:118px;top:3896px;width:320px;height:466px;background:var(--teal);border-radius:14px;color:var(--white)}
.contact-card h2{position:absolute;left:42px;top:70px;font-size:38px;color:var(--white)}
.cline{position:absolute;left:42px;display:flex;align-items:center;gap:10px;font-size:14px;font-weight:500}
.divider{position:absolute;left:42px;width:238px;border-top:1px solid #7c979a}
.form-title{left:478px;top:3884px;font-size:20px;font-weight:500;color:#333}
.flabel{left:478px;font-size:13px;font-weight:600;color:#333}
.field{left:478px;width:579px;height:31px;border:1px solid #aaa;border-radius:3px;font-size:11px;color:#999;padding:8px 13px}
.send{left:478px;top:4319px;width:579px;height:31px}

/* footer */
.foot-sky{left:0;top:4458px;width:1200px;height:464px;background:linear-gradient(180deg,#fff 0%,#edf1f2 25%,#e6ebec 70%,#f3f5f5 100%)}
.foot-brand{left:0;width:1200px;top:4560px;text-align:center;font-size:30px;font-weight:600;color:#1d2a2c}
.foot-nav{left:0;width:1200px;top:4660px;display:flex;justify-content:center;gap:34px;font-size:13px;color:#333}
.foot-nav span:first-child{color:var(--orange)}
.foot-contact{left:0;width:1200px;top:4706px;display:flex;justify-content:center;gap:22px;font-size:13px;color:#333}
.foot-contact span{display:flex;align-items:center;gap:6px}
.foot-social{left:0;width:1200px;top:4744px;display:flex;justify-content:center;gap:22px}
.copy{left:0;width:1200px;top:4796px;text-align:center;font-size:13px;color:#333}
</style>
</head>
<body>

<!-- header -->
<div class="abs brand">Quill<br>Vantor</div>
<div class="abs topbar">
  <span><svg width="17" height="14" viewBox="0 0 17 14"><path d="M1 5 8.5 1 16 5v8H1z" fill="#2e5358"/><path d="M1 5l7.5 5L16 5" stroke="#fff" fill="none"/></svg>info@quillvantor.com</span>
  <span><svg width="15" height="15" viewBox="0 0 24 24"><path d="M6.6 10.8a15 15 0 0 0 6.6 6.6l2.2-2.2a1 1 0 0 1 1-.25 11 11 0 0 0 3.6.6 1 1 0 0 1 1 1V20a1 1 0 0 1-1 1A17 17 0 0 1 3 4a1 1 0 0 1 1-1h3.5a1 1 0 0 1 1 1 11 11 0 0 0 .6 3.6 1 1 0 0 1-.25 1z" fill="#2e5358"/></svg>+1 5550 182 407</span>
  <i class="social-dot"></i><i class="social-dot"></i><i class="social-dot"></i>
</div>
<div class="btn inquiry"><i class="dot"></i>Inquiry Form</div>
<nav class="abs nav"><a>Home</a><a>About</a><a>How it works</a><a>Products</a><a>Pricing</a><a>Contact Us</a></nav>

<!-- hero -->
<div class="abs hero-sky" role="img" aria-label="Soft cloudy sky backdrop"></div>
<svg class="abs hero-art" width="760" height="453" viewBox="0 0 760 453" role="img" aria-label="Woman on a phone call surrounded by digital security icons">
  <defs><linearGradient id="heroG" x1="0" y1="0" x2="1" y2="1"><stop offset="0" stop-color="#dfe6e8"/><stop offset=".55" stop-color="#c6d3d7"/><stop offset="1" stop-color="#9fb4ba"/></linearGradient></defs>
  <path d="M80 0C10 150 60 390 330 453L760 453 760 0Z" fill="url(#heroG)"/>
  <path d="M80 0C10 150 60 390 330 453" fill="none" stroke="#2e5358" stroke-width="6"/>
</svg>
<h1 class="abs display hero-title">Welcome To<br>Quill Vantor</h1>
<p class="abs hero-sub">We Protect Your <b>Cyber Guardian</b> | All The Time</p>
<div class="btn hero-btn"><i class="dot"></i>Get Started Now</div>

<div class="abs offer" style="left:53px">
  <svg width="118" height="130" viewBox="0 0 118 130" fill="none" stroke="#fff" stroke-width="3"><rect x="6" y="40" width="100" height="66" rx="4"/><path d="M40 106v12h32v-12M30 120h52"/><rect x="20" y="52" width="40" height="40"/><circle cx="80" cy="30" r="20"/></svg>
  <h3>Quill Vantor For Business</h3>
  <p>Lorem ipsum dolor sit amet, consectetur adipiscing elit. Ut elit tellus, luctus nec ullamcorper mattis, pulvinar dapibus leo.</p>
  <span class="more">⊕ Get Started Now</span>
</div>
<div class="abs offer" style="left:627px">
  <svg width="118" height="130" viewBox="0 0 118 130" fill="none" stroke="#fff" stroke-width="3"><rect x="6" y="40" width="100" height="66" rx="4"/><path d="M40 106v12h32v-12M30 120h52"/><circle cx="56" cy="42" r="24"/><rect x="48" y="40" width="16" height="14"/></svg>
  <h3>Quill Vantor For Home</h3>
  <p>Lorem ipsum dolor sit amet, consectetur adipiscing elit. Ut elit tellus, luctus nec ullamcorper mattis, pulvinar dapibus leo.</p>
  <span class="more">⊕ Get Started Now</span>
</div>

<!-- about -->
<svg class="abs orbit" width="540" height="540" viewBox="0 0 540 540" role="img" aria-label="Businessman with network graphics surrounded by photos of people working at computers">
  <defs><radialGradient id="ab" cx=".5" cy=".45" r=".6"><stop offset="0" stop-color="#5b8fb8"/><stop offset="1" stop-color="#1d3d5c"/></radialGradient></defs>
  <circle cx="235" cy="278" r="184" fill="none" stroke="#2e5358" stroke-width="4"/>
  <circle cx="235" cy="278" r="176" fill="url(#ab)"/>
  <circle cx="120" cy="55" r="55" fill="#243a52" stroke="#2e5358" stroke-width="5"/>
  <circle cx="480" cy="250" r="52" fill="#3b4c5e" stroke="#2e5358" stroke-width="5"/>
  <circle cx="55" cy="480" r="52" fill="#4a5968" stroke="#2e5358" stroke-width="5"/>
  <circle cx="420" cy="470" r="60" fill="#5a4f4a" stroke="#2e5358" stroke-width="5"/>
</svg>
<h2 class="abs display about-title">About Quill Vantor</h2>
<p class="abs about-text">Welcome to Quill Vantor, your trusted partner in cybersecurity. Founded by experts with decades of experience in digital security, Quill Vantor is committed to protecting businesses of all sizes from cyber threats. We specialize in proactive cybersecurity measures, providing innovative solutions to safeguard your digital assets. Our mission is to help you navigate the complexities of cybersecurity, ensuring your business stays secure and resilient in an increasingly digital world.</p>
<div class="btn about-btn"><i class="dot"></i>Contact Us Now</div>

<!-- how it works -->
<div class="abs how-band"></div>
<h2 class="abs display how-title">How It Works?</h2>
<p class="abs how-intro">At Quill Vantor, we believe in a proactive approach to cybersecurity. Our process is designed to identify, assess, and mitigate potential threats before they can impact your business. Here’s how it works:</p>
<div class="abs step" style="left:48px">
  <svg width="64" height="66" viewBox="0 0 64 66" fill="none" stroke="#2e5358" stroke-width="2"><rect x="8" y="4" width="40" height="54"/><circle cx="30" cy="32" r="13"/><path d="M39 41l16 16"/></svg>
  <h4>1: Assessment</h4>
  <p>We begin with a thorough assessment of your current cybersecurity posture, identifying vulnerabilities and potential threats.</p>
</div>
<div class="abs step" style="left:324px">
  <svg width="64" height="66" viewBox="0 0 64 66" fill="none" stroke="#2e5358" stroke-width="2"><circle cx="32" cy="26" r="16"/><path d="M25 44h14v10H25zM32 2v4M8 26h4M52 26h4"/></svg>
  <h4>2: Customized Solutions</h4>
  <p>Based on our assessment, we develop a customized cybersecurity strategy tailored to your business needs. This includes selecting the right products and services from our comprehensive suite.</p>
</div>
<div class="abs step" style="left:604px">
  <svg width="64" height="66" viewBox="0 0 64 66" fill="none" stroke="#2e5358" stroke-width="2"><rect x="4" y="28" width="34" height="32"/><circle cx="46" cy="20" r="12"/><circle cx="46" cy="20" r="4"/><path d="M12 38h18M12 48h18"/></svg>
  <h4>3: Implementation</h4>
  <p>Our team of experts implements the chosen solutions, ensuring seamless integration with your existing systems.</p>
</div>
<div class="abs step" style="left:882px">
  <svg width="64" height="66" viewBox="0 0 64 66" fill="none" stroke="#2e5358" stroke-width="2"><rect x="4" y="8" width="56" height="40" rx="3"/><path d="M24 48v10h16V48M18 60h28"/><circle cx="32" cy="28" r="10"/></svg>
  <h4>4: Monitoring &amp; Support:</h4>
  <p>We provide continuous monitoring and support to detect and respond to any security incidents in real time. Our team is available 24/7 to assist with any issues that may arise.</p>
</div>

<!-- products -->
<h2 class="abs display prod-title">Our Products</h2>
<div class="abs box" style="left:179px" role="img" aria-label="QuillGuard product box"><svg width="160" height="230"><defs><linearGradient id="bx" x1="0" x2="1"><stop offset="0" stop-color="#1f2b2d"/><stop offset=".25" stop-color="#2a3a3d"/><stop offset="1" stop-color="#44575a"/></linearGradient></defs><path d="M0 18 150 0 160 210 10 230Z" fill="url(#bx)"/></svg></div>
<div class="abs box" style="left:520px" role="img" aria-label="Cyber Orbit 360 product box"><svg width="160" height="230"><path d="M4 10 160 0 156 230 0 222Z" fill="url(#bx)"/></svg></div>
<div class="abs box" style="left:848px" role="img" aria-label="SafeLetter product box"><svg width="160" height="230"><path d="M0 20 150 0 158 222 6 230Z" fill="url(#bx)"/></svg></div>

<p class="abs prod-name" style="left:35px">QuillGuard</p>
<p class="abs prod-name" style="left:454px">Cyber Orbit 360</p>
<p class="abs prod-name" style="left:780px">SafeLetter</p>

<ul class="abs features" style="left:153px">
  <li><b>Automated Patch Management</b><span class="j">Automatically applies security patches to your systems, ensuring they are up-to-date with the latest protections.</span></li>
  <li><b>Vulnerability Scanning</b><span class="j">Identifies and assesses vulnerabilities in your software and systems, prioritizing patches based on risk level.</span></li>
  <li><b>Centralized Dashboard</b><span class="j">Provides a user-friendly interface for managing and monitoring patch status across all devices and applications.</span></li>
  <li><b>Scheduled Updates</b><span class="j">Allows scheduling of patch deployments at convenient times, minimizing disruption to business operations.</span></li>
</ul>
<ul class="abs features" style="left:482px">
  <li><b>Comprehensive Threat Detection</b>Identifies and mitigates a wide range of cyber threats, including malware, ransomware, and phishing attacks.</li>
  <li><b>Advanced Firewall Protection</b>Blocks unauthorized access and controls incoming and outgoing network traffic based on predetermined security rules.</li>
  <li><b>Intrusion Detection and Prevention</b>Monitors network traffic for suspicious activity and automatically takes action to prevent potential intrusions.</li>
  <li><b>Real-Time Threat Intelligence</b>Provides up-to-date information on emerging threats and vulnerabilities, helping to stay ahead of cybercriminals.</li>
</ul>
<ul class="abs features" style="left:810px">
  <li><b>End-to-End Encryption</b>Ensures all email communications are encrypted, protecting the content from unauthorized access.</li>
  <li><b>Advanced Threat Protection</b>Guards against phishing, malware, and other cyber threats, preventing malicious emails from reaching your inbox.</li>
  <li><b>Secure Attachments</b>Encrypts attachments, ensuring sensitive documents are protected during transmission.</li>
  <li><b>Two-Factor Authentication (2FA)</b>Adds an extra layer of security by requiring a second form of verification before accessing emails.</li>
</ul>

<!-- pricing -->
<h2 class="abs display price-title">Our Pricing</h2>
<svg width="0" height="0" style="position:absolute"><defs>
  <symbol id="tick" viewBox="0 0 16 14"><path d="M1 7l5 5L15 1" stroke="#f7811d" stroke-width="2" fill="none"/></symbol>
  <symbol id="cross" viewBox="0 0 16 14"><path d="M3 2l10 10M13 2 3 12" stroke="#fff" stroke-width="1.6" fill="none"/></symbol>
</defs></svg>

<div class="abs plan" style="left:67px">
  <h3>Lite</h3><hr><p class="amt">$65<small>/Year</small></p>
  <ul>
    <li><svg width="16" height="14"><use href="#tick"/></svg>Comprehensive Threat Detection</li>
    <li><svg width="16" height="14"><use href="#tick"/></svg>Advanced Firewall Protection</li>
    <li><svg width="16" height="14"><use href="#tick"/></svg>Intrusion Detection and Prevention</li>
    <li><svg width="16" height="14"><use href="#tick"/></svg>Real-Time Threat Intelligence</li>
    <li><svg width="16" height="14"><use href="#cross"/></svg>Behavioral Analysis</li>
    <li><svg width="16" height="14"><use href="#cross"/></svg>Data Encryption</li>
    <li><svg width="16" height="14"><use href="#cross"/></svg>Web Filtering</li>
    <li><svg width="16" height="14"><use href="#cross"/></svg>Multi-Layered Security</li>
    <li><svg width="16" height="14"><use href="#cross"/></svg>24/7 Monitoring and Response</li>
  </ul>
</div>
<div class="abs plan" style="left:438px">
  <h3>Medium</h3><hr><p class="amt">$85<small>/Year</small></p>
  <ul>
    <li><svg width="16" height="14"><use href="#tick"/></svg>Comprehensive Threat Detection</li>
    <li><svg width="16" height="14"><use href="#tick"/></svg>Advanced Firewall Protection</li>
    <li><svg width="16" height="14"><use href="#tick"/></svg>Intrusion Detection and Prevention</li>
    <li><svg width="16" height="14"><use href="#tick"/></svg>Real-Time Threat Intelligence</li>
    <li><svg width="16" height="14"><use href="#tick"/></svg>Behavioral Analysis</li>
    <li><svg width="16" height="14"><use href="#tick"/></svg>Data Encryption</li>
    <li><svg width="16" height="14"><use href="#cross"/></svg>Web Filtering</li>
    <li><svg width="16" height="14"><use href="#cross"/></svg>Multi-Layered Security</li>
    <li><svg width="16" height="14"><use href="#cross"/></svg>24/7 Monitoring and Response</li>
  </ul>
</div>
<div class="abs plan" style="left:808px">
  <div class="ribbon">POPULAR</div>
  <h3>Professional</h3><hr><p class="amt">$110<small>/Year</small></p>
  <ul>
    <li><svg width="16" height="14"><use href="#tick"/></svg>Comprehensive Threat Detection</li>
    <li><svg width="16" height="14"><use href="#tick"/></svg>Advanced Firewall Protection</li>
    <li><svg width="16" height="14"><use href="#tick"/></svg>Intrusion Detection and Prevention</li>
    <li><svg width="16" height="14"><use href="#tick"/></svg>Real-Time Threat Intelligence</li>
    <li><svg width="16" height="14"><use href="#tick"/></svg>Behavioral Analysis</li>
    <li><svg width="16" height="14"><use href="#tick"/></svg>Data Encryption</li>
    <li><svg width="16" height="14"><use href="#tick"/></svg>Web Filtering</li>
    <li><svg width="16" height="14"><use href="#tick"/></svg>Multi-Layered Security</li>
    <li><svg width="16" height="14"><use href="#tick"/></svg>24/7 Monitoring and Response</li>
  </ul>
</div>

<!-- contact -->
<div class="abs contact-card">
  <h2 class="display">Contact Us</h2>
  <div class="cline" style="top:124px"><svg width="14" height="18" viewBox="0 0 14 18"><path d="M7 0a7 7 0 0 1 7 7c0 5-7 11-7 11S0 12 0 7a7 7 0 0 1 7-7z" fill="#fff"/><circle cx="7" cy="7" r="2.5" fill="#2e5358"/></svg>#48 Corvel Court, Sydney, AU</div>
  <div class="divider" style="top:177px"></div>
  <div class="cline" style="top:212px"><svg width="17" height="14" viewBox="0 0 17 14"><path d="M1 5 8.5 1 16 5v8H1z" fill="#fff"/><path d="M1 5l7.5 5L16 5" stroke="#2e5358" fill="none"/></svg>info@quillvantor.com</div>
  <div class="divider" style="top:266px"></div>
  <div class="cline" style="top:300px"><svg width="15" height="15" viewBox="0 0 24 24"><path d="M6.6 10.8a15 15 0 0 0 6.6 6.6l2.2-2.2a1 1 0 0 1 1-.25 11 11 0 0 0 3.6.6 1 1 0 0 1 1 1V20a1 1 0 0 1-1 1A17 17 0 0 1 3 4a1 1 0 0 1 1-1h3.5a1 1 0 0 1 1 1 11 11 0 0 0 .6 3.6 1 1 0 0 1-.25 1z" fill="#fff"/></svg>+1 5550 182 407</div>
  <div class="divider" style="top:352px"></div>
  <div class="cline" style="top:382px;gap:18px"><i class="social-dot" style="background:#fff"></i><i class="social-dot" style="background:#fff"></i><i class="social-dot" style="background:#fff"></i></div>
</div>

<h3 class="abs form-title">Inquiry Form</h3>
<label class="abs flabel" style="top:3946px">Name</label>
<div class="abs field" style="top:3970px">Name</div>
<label class="abs flabel" style="top:4010px">Phone</label>
<div class="abs field" style="top:4034px">Your Phone Number</div>
<label class="abs flabel" style="top:4075px">Email</label>
<div class="abs field" style="top:4099px">Your Email</div>
<label class="abs flabel" style="top:4140px">Subject</label>
<div class="abs field" style="top:4164px">Type Subject</div>
<label class="abs flabel" style="top:4205px">Message</label>
<div class="abs field" style="top:4229px;height:80px">Type Your Message</div>
<div class="btn send"><i class="dot"></i>Send Your Message</div>

<!-- footer -->
<div class="abs foot-sky" role="img" aria-label="Soft cloudy sky backdrop"></div>
<p class="abs foot-brand">Quill Vantor</p>
<div class="abs foot-nav"><span>Home</span><span>About</span><span>How it works</span><span>Products</span><span>Pricing</span><span>Contact Us</span></div>
<div class="abs foot-contact">
  <span><svg width="11" height="14" viewBox="0 0 14 18"><path d="M7 0a7 7 0 0 1 7 7c0 5-7 11-7 11S0 12 0 7a7 7 0 0 1 7-7z" fill="#2e5358"/></svg>#48 Corvel Court, Sydney, AU</span>
  <span><svg width="14" height="12" viewBox="0 0 17 14"><path d="M1 5 8.5 1 16 5v8H1z" fill="#2e5358"/></svg>info@quillvantor.com</span>
  <span><svg width="13" height="13" viewBox="0 0 24 24"><path d="M6.6 10.8a15 15 0 0 0 6.6 6.6l2.2-2.2a1 1 0 0 1 1-.25 11 11 0 0 0 3.6.6 1 1 0 0 1 1 1V20a1 1 0 0 1-1 1A17 17 0 0 1 3 4a1 1 0 0 1 1-1h3.5a1 1 0 0 1 1 1 11 11 0 0 0 .6 3.6 1 1 0 0 1-.25 1z" fill="#2e5358"/></svg>+1 5550 182 407</span>
</div>
<div class="abs foot-social"><i class="social-dot"></i><i class="social-dot"></i><i class="social-dot"></i></div>
<p class="abs copy">Copyright © 2024 quillvantor | Powered by quillvantor</p>

</body>
</html>
```